New York College Admissions Consulting Company Looking for a One-Page Flyer Design

We are a college admissions consulting company Harwick Admissions Consulting (www.harwickadmissions.example) and we help students apply to universities. We need a 1-page flyer design to hand out at a science competition for high school students. I attach all the information that should be included in the flyer and the logo. Please make a stylistic and professional looking flyer, which will impress these very smart and sophisticated high school students and even more importantly - their parents. Feel free to move the text around the flyer and to change the font as you see fit. Also, please add a stock picture or two, as you see fit. Also, let me know if I have to pay for the stock photos (if I have to get a license to use the photos on the flyer), and where and how much I would need to pay.

Target Market(s)

Smart and sophisticated high school students and even more importantly - their parents.

Industry/Entity Type

College

Requirements
Must have
• Must look sophisticated. This is an expensive service and parents need to know that our image matches our prices.
Should not have
• Wild colors like red.

```html
<!DOCTYPE html>
<html lang="en">
<head>
<meta charset="utf-8">
<title>The Personal Statement – Complimentary Live Online Class</title>
<link rel="stylesheet" href="https://fonts.googleapis.com/css2?family=Open+Sans:wght@600;700;800&family=Roboto+Condensed:wght@700&display=swap">
<style>
  :root {
    --navy: #1b2d4f;
    --steel: #2f5586;
    --bronze: #8c7048;
    --brand-blue: #2a5c96;
    --white: #ffffff;
    --paper: #ffffff;
    --photo-desk-a: #e9e6e2;
    --photo-desk-b: #b9b3ad;
    --photo-crowd-a: #c9d3c0;
    --photo-crowd-b: #d7a067;
    --photo-crowd-c: #6d86a8;
  }
  * { box-sizing: border-box; margin: 0; padding: 0; }
  html, body { width: 863px; height: 1200px; overflow: hidden; background: var(--paper); }
  .flyer {
    position: relative;
    width: 863px;
    height: 1200px;
    background: var(--paper);
    font-family: "Open Sans", Arial, sans-serif;
    color: var(--white);
  }
  .band-top {
    position: absolute; left: 0; top: 0; width: 863px; height: 130px;
    background: var(--navy);
    display: flex; align-items: center; justify-content: center;
    font-weight: 700; font-size: 41px; letter-spacing: 0.2px;
  }
  .class-title {
    position: absolute; left: 0; top: 138px; width: 863px;
    text-align: center; color: var(--navy);
    font-weight: 700; font-size: 43px; line-height: 50px;
  }
  .photo { position: absolute; }
  .photo-essay {
    left: 0; top: 250px; width: 405px; height: 265px;
    background: linear-gradient(135deg, var(--photo-desk-a) 0%, #f6f4f1 45%, var(--photo-desk-b) 100%);
  }
  .photo-students {
    left: 0; top: 515px; width: 405px; height: 475px;
    background: linear-gradient(180deg, var(--photo-crowd-a) 0%, var(--photo-crowd-b) 45%, var(--photo-crowd-c) 80%, #a9a39b 100%);
  }
  .photo-strip {
    left: 405px; top: 596px; width: 458px; height: 32px;
    background: linear-gradient(90deg, #d8c2a8 0%, #b99475 50%, #cbb9a3 100%);
  }
  .panel-learn {
    position: absolute; left: 407px; top: 250px; width: 456px; height: 181px;
    background: var(--steel);
    padding: 8px 0 0 10px;
  }
  .panel-learn h2 { font-weight: 700; font-size: 26px; line-height: 32px; margin-bottom: 2px; }
  .checklist { list-style: none; }
  .checklist li {
    display: flex; font-weight: 600; font-size: 21px; line-height: 27px; margin-bottom: 6px;
  }
  .checklist li:last-child { margin-top: 8px; }
  .checklist svg { flex: 0 0 auto; margin: 6px 8px 0 2px; }
  .panel-live {
    position: absolute; left: 407px; top: 437px; width: 456px; height: 159px;
    background: var(--bronze);
    text-align: center; padding-top: 8px;
  }
  .panel-live h2 { font-weight: 700; font-size: 40px; line-height: 46px; }
  .panel-live .date { font-weight: 700; font-size: 24px; margin-top: 4px; }
  .panel-facts {
    position: absolute; left: 407px; top: 628px; width: 456px; height: 362px;
    background: var(--steel);
    padding: 20px 8px 0 10px;
  }
  .panel-facts h2 { font-weight: 700; font-size: 26px; line-height: 32px; margin-bottom: 2px; }
  .facts { list-style: none; font-family: "Roboto Condensed", "Arial Narrow", sans-serif; font-weight: 700; font-size: 20px; line-height: 26px; }
  .facts li { position: relative; padding-left: 14px; margin-bottom: 1px; }
  .facts li::before {
    content: ""; position: absolute; left: 1px; top: 10px; width: 7px; height: 7px; border-radius: 50%; background: var(--white);
  }
  .brand {
    position: absolute; left: 0; top: 990px; width: 863px; height: 85px;
    display: flex; align-items: center; justify-content: center; gap: 14px;
    color: var(--brand-blue); font-weight: 600; font-size: 31px;
  }
  .brand .mark { width: 16px; height: 16px; border-radius: 50%; background: var(--brand-blue); }
  .band-bottom {
    position: absolute; left: 0; top: 1078px; width: 863px; height: 122px;
    background: var(--navy);
    text-align: center; padding-top: 14px;
    font-weight: 700; font-size: 24px; line-height: 35px;
  }
</style>
</head>
<body>
<div class="flyer">
  <header class="band-top">Complimentary Live Online Class</header>

  <h1 class="class-title">“The Personal Statement<br>Perfecting Your Narrative”</h1>

  <div class="photo photo-essay" role="img" aria-label="Close-up of a hand writing with a pen on a college application essay"></div>
  <div class="photo photo-students" role="img" aria-label="Group of cheerful students jumping in the air outdoors"></div>
  <div class="photo photo-strip" role="img" aria-label="Strip of students gathered together"></div>

  <section class="panel-learn">
    <h2>Learn How To</h2>
    <ul class="checklist">
      <li><svg width="15" height="15" viewBox="0 0 15 15" aria-hidden="true"><rect x="0.75" y="0.75" width="13.5" height="13.5" fill="none" stroke="#fff" stroke-width="1.5"/><path d="M3 7.5l3 3 6-7" fill="none" stroke="#fff" stroke-width="1.8"/></svg><span>Avoid the Most Common Mistakes<br>Made in The Personal Statement</span></li>
      <li><svg width="15" height="15" viewBox="0 0 15 15" aria-hidden="true"><rect x="0.75" y="0.75" width="13.5" height="13.5" fill="none" stroke="#fff" stroke-width="1.5"/><path d="M3 7.5l3 3 6-7" fill="none" stroke="#fff" stroke-width="1.8"/></svg><span>Compose a Memorable Essay</span></li>
      <li><svg width="15" height="15" viewBox="0 0 15 15" aria-hidden="true"><rect x="0.75" y="0.75" width="13.5" height="13.5" fill="none" stroke="#fff" stroke-width="1.5"/><path d="M3 7.5l3 3 6-7" fill="none" stroke="#fff" stroke-width="1.8"/></svg><span>Craft a Compelling Narrative</span></li>
    </ul>
  </section>

  <section class="panel-live">
    <h2>Live Answers<br>to Live Questions</h2>
    <p class="date">Sunday, May 13, 2015</p>
  </section>

  <section class="panel-facts">
    <h2>Admission Facts and Tips</h2>
    <ul class="facts">
      <li>In the lst 9 years, the Average Ivy League<br>College Admission Rate has dropped by 49%.</li>
      <li>Admission Rate in 2005 - 17.1%</li>
      <li>Admission Rate in 2014 - 8.8%</li>
      <li>The Personal Statement and the<br>Supplemental Essays comprise approximately<br>25% of the admission criteria</li>
      <li>Crafting the Perfect Narrative is vital to your<br>college application. It can mean the difference<br>between an acceptance and a rejection.</li>
    </ul>
  </section>

  <div class="brand"><span class="mark"></span><span>Harwick Admissions Consulting</span></div>

  <footer class="band-bottom">
    <p>www.harwickadmissions.example</p>
    <p>1.646.555.0142</p>
  </footer>
</div>
</body>
</html>
```